We are a building company that build new homes and units we are looking for something fresh and looks good my company name is
Orland Building Group Pty Ltd

Industry/Entity Type

Building

Contact Information for Business Card

Name Marco Deluca-Finn
Tittle: Director
Address 14 Larkmoor St. Pellingwood Vic 3091
Ph: 03 9512 4386
Mobile : 0400 736 294

www.orlandbuildinggroup.com.au
Email: sales@orlandbuildinggroup.com.au

```html
<!DOCTYPE html>
<html lang="en">
<head>
<meta charset="utf-8">
<title>Orland Building Group – Business Card</title>
<link rel="stylesheet" href="https://fonts.googleapis.com/css2?family=Open+Sans:wght@400;700&display=swap">
<style>
  :root {
    --page-bg: #e9e9ea;
    --card-brown-top: #8c7a6b;
    --card-brown-bottom: #5b4738;
    --ink-light: #ffffff;
    --ink-soft: rgba(255,255,255,0.88);
    --photo-dark: #2e2a24;
    --photo-mid: #6b5a44;
  }
  * { box-sizing: border-box; margin: 0; padding: 0; }
  html, body {
    width: 1200px; height: 720px; overflow: hidden;
    background: var(--page-bg);
    font-family: "Open Sans", Arial, sans-serif;
  }
  .canvas {
    width: 1200px; height: 720px;
    display: flex; align-items: center; justify-content: center; gap: 40px;
  }
  .card {
    position: relative;
    width: 540px; height: 300px;
    overflow: hidden;
    box-shadow: 0 6px 18px rgba(0,0,0,0.18);
  }

  /* Contact side */
  .card--contact {
    background: linear-gradient(180deg, var(--card-brown-top) 0%, var(--card-brown-bottom) 100%);
    color: var(--ink-light);
  }
  .divider {
    position: absolute; left: 264px; top: 48px; bottom: 0;
    width: 2px; background: var(--ink-light);
  }
  .company-line {
    position: absolute; left: 22px; bottom: 26px; width: 230px;
    font-size: 12.5px; letter-spacing: 0.1px;
    text-transform: uppercase; white-space: nowrap;
  }
  .company-line strong { font-weight: 700; }
  .company-line span { font-weight: 400; }
  .person {
    position: absolute; left: 284px; top: 44px; right: 12px;
  }
  .person__name {
    font-size: 17px; font-weight: 700; text-transform: uppercase; letter-spacing: 0.3px;
    white-space: nowrap;
  }
  .person__title { font-size: 13px; color: var(--ink-soft); margin-top: 1px; }
  .person__address { font-size: 10px; color: var(--ink-soft); margin-top: 22px; white-space: nowrap; }
  .contact-list { list-style: none; margin-top: 20px; }
  .contact-list li {
    display: flex; align-items: center; gap: 11px;
    font-size: 11.5px; color: var(--ink-soft); line-height: 20px; white-space: nowrap;
  }
  .contact-list svg { width: 13px; height: 13px; flex: none; }

  /* Brand side */
  .card--brand { background: var(--photo-dark); }
  .brand-photo {
    position: absolute; inset: 0;
    background:
      radial-gradient(ellipse at 18% 70%, rgba(214,196,160,0.75) 0%, rgba(214,196,160,0) 45%),
      radial-gradient(ellipse at 78% 25%, rgba(190,170,140,0.55) 0%, rgba(190,170,140,0) 40%),
      linear-gradient(160deg, var(--photo-mid) 0%, var(--photo-dark) 70%, #1f2226 100%);
  }
  .brand-frame {
    position: absolute; left: 175px; top: 160px;
    width: 335px; height: 74px;
    border: 2px solid rgba(255,255,255,0.9);
    display: flex; align-items: center; justify-content: center;
    color: rgba(255,255,255,0.92);
    font-size: 16px; text-transform: uppercase; white-space: nowrap;
  }
  .brand-frame strong { font-weight: 700; margin-right: 6px; }
  .brand-frame span { font-weight: 400; }
</style>
</head>
<body>
<main class="canvas">
  <section class="card card--contact" aria-label="Business card, contact side">
    <div class="divider"></div>
    <p class="company-line"><strong>Orland Building Group</strong> <span>Pty Ltd</span></p>
    <div class="person">
      <h1 class="person__name">Marco Deluca-Finn</h1>
      <p class="person__title">Director</p>
      <p class="person__address">14 Larkmoor St. Pellingwood Vic 3091</p>
      <ul class="contact-list">
        <li>
          <svg viewBox="0 0 24 24" aria-hidden="true"><path fill="#fff" d="M6.6 10.8a15.1 15.1 0 0 0 6.6 6.6l2.2-2.2c.3-.3.7-.4 1-.2 1.1.4 2.3.6 3.6.6.6 0 1 .4 1 1V20c0 .6-.4 1-1 1A17 17 0 0 1 3 4c0-.6.4-1 1-1h3.5c.6 0 1 .4 1 1 0 1.3.2 2.5.6 3.6.1.3 0 .7-.2 1z"/></svg>
          <span>03 9512 4386</span>
        </li>
        <li>
          <svg viewBox="0 0 24 24" aria-hidden="true"><rect x="6" y="2" width="12" height="20" rx="2" fill="none" stroke="#fff" stroke-width="2"/><circle cx="12" cy="18" r="1.2" fill="#fff"/></svg>
          <span>0400 736 294</span>
        </li>
        <li>
          <svg viewBox="0 0 24 24" aria-hidden="true"><rect x="2" y="5" width="20" height="14" fill="#fff"/><path d="M2 5l10 8 10-8" fill="none" stroke="#5b4738" stroke-width="1.6"/></svg>
          <span>sales@orlandbuildinggroup.com.au</span>
        </li>
        <li>
          <svg viewBox="0 0 24 24" aria-hidden="true"><g fill="none" stroke="#fff" stroke-width="1.6"><circle cx="12" cy="12" r="9.5"/><ellipse cx="12" cy="12" rx="4" ry="9.5"/><path d="M2.5 12h19M4 7h16M4 17h16"/></g></svg>
          <span>www.orlandbuildinggroup.com.au</span>
        </li>
      </ul>
    </div>
  </section>

  <section class="card card--brand" aria-label="Business card, brand side">
    <div class="brand-photo" role="img" aria-label="Photograph of a warmly lit luxury bedroom interior with a canopy bed, timber doors and window blinds"></div>
    <p class="brand-frame"><strong>Orland Building Group</strong><span>Pty Ltd</span></p>
  </section>
</main>
</body>
</html>
```